Need Flyer for Our Real estate Agency

Need to run General Campaign for our agency with Start of New Year as our theme ..Must have an agent's picture on the DL..
Address:
9 / 386Barwin rd, Truganina VIC 3029
Ph:03 9142 7305
email:info@koridanrealestate.example.au
www.koridanrealestate.example.au
Something like as attached picture..
Target Market(s)
Home Buyers
Industry/Entity Type
Real Estate Agent
Requirements
Must have
- Our Logo Colours

```html
<!DOCTYPE html>
<html lang="en">
<head>
<meta charset="utf-8">
<title>Koridan Real Estate – New Year DL Flyer</title>
<link rel="stylesheet" href="https://fonts.googleapis.com/css2?family=Lato:wght@300;400;700&display=swap">
<style>
  :root {
    --navy-deep: #0c2a5e;
    --navy: #12397f;
    --blue-bright: #1a5cb0;
    --maroon: #7a1420;
    --white: #ffffff;
    --grey-arc: #c9ccd2;
    --page: #e9e9e9;
    --photo-light: #a3b1c6;
    --photo-dark: #6f7f86;
    --portrait-light: #55699a;
    --portrait-dark: #2c4a8c;
  }
  * { box-sizing: border-box; margin: 0; padding: 0; }
  html, body { width: 1200px; height: 1196px; overflow: hidden; }
  body {
    background: var(--page);
    font-family: "Lato", Arial, sans-serif;
    color: var(--white);
    position: relative;
  }
  .flyer {
    position: absolute;
    left: 111px;
    width: 964px;
    height: 459px;
    overflow: hidden;
    box-shadow: 0 4px 14px rgba(0,0,0,.25);
  }
  .flyer--front { top: 113px; background: linear-gradient(120deg, var(--navy-deep), var(--navy) 60%, var(--navy-deep)); }
  .flyer--back { top: 643px; height: 457px; background: linear-gradient(90deg, var(--blue-bright), var(--navy) 55%, var(--navy-deep)); }

  .front-art { position: absolute; inset: 0; }

  .brand {
    position: absolute;
    text-align: center;
    color: var(--white);
    font-weight: 400;
  }
  .brand__name { display: block; font-size: 46px; letter-spacing: 5px; line-height: 1; }
  .brand__sub { display: block; font-size: 11px; letter-spacing: 4px; margin-top: 8px; }
  .front .brand { left: 480px; width: 440px; top: 122px; }

  .headline {
    position: absolute; left: 480px; width: 440px; top: 212px;
    text-align: center; font-weight: 300; font-size: 32px; line-height: 45px;
  }
  .teaser {
    position: absolute; left: 444px; width: 512px; top: 323px;
    text-align: center; font-size: 15px; font-weight: 400;
  }
  .teaser strong { font-weight: 700; }

  .cta {
    position: absolute; left: 519px; top: 371px; width: 362px; height: 47px;
    background: var(--white); border-radius: 24px;
    box-shadow: 0 3px 8px rgba(0,0,0,.3);
    display: flex; align-items: center; justify-content: center; gap: 8px;
    color: var(--maroon); font-weight: 700; font-size: 20px;
  }
  .cta svg { width: 20px; height: 20px; }
  .cta__note {
    position: absolute; left: 519px; width: 362px; top: 425px;
    text-align: center; font-size: 17px; font-weight: 300;
  }

  .back .brand { left: 60px; width: 270px; top: 126px; }
  .contact-list { position: absolute; left: 70px; top: 222px; list-style: none; }
  .contact-list li {
    display: flex; align-items: center; gap: 12px;
    font-size: 17px; font-weight: 300; height: 41px;
  }
  .contact-list svg { width: 18px; height: 18px; flex: none; }

  .agent-photo {
    position: absolute; left: 648px; top: 7px; width: 286px; height: 383px;
    background: linear-gradient(180deg, var(--portrait-light), var(--portrait-dark));
  }

  .footer-band {
    position: absolute; left: 0; right: 0; bottom: 0; height: 67px;
    background: var(--maroon); border-top: 3px solid var(--white);
    display: flex; align-items: center; justify-content: space-between;
    padding: 0 56px 0 72px;
  }
  .footer-band__address { font-size: 17px; font-weight: 300; }
  .footer-band__agent { font-size: 22px; font-weight: 700; }
</style>
</head>
<body>

<section class="flyer flyer--front front">
  <svg class="front-art" viewBox="0 0 964 459" width="964" height="459">
    <defs>
      <linearGradient id="houseTones" x1="0" y1="0" x2="0" y2="1">
        <stop offset="0" stop-color="var(--photo-light)"/>
        <stop offset="1" stop-color="var(--photo-dark)"/>
      </linearGradient>
    </defs>
    <path class="front-art__band" d="M0 391 H 964 V 459 H 0 Z" fill="var(--maroon)"/>
    <path d="M0 391 H 964" stroke="var(--white)" stroke-width="3"/>
    <path class="front-art__arc" d="M285 0 H 395 C 458 110, 458 330, 392 459 H 370 C 418 330, 405 90, 285 0 Z" fill="var(--grey-arc)"/>
    <path role="img" aria-label="Photo of the agent in a suit standing in front of a two-storey family home"
          d="M0 0 H 280 C 400 85, 416 330, 366 459 H 0 Z" fill="url(#houseTones)"/>
    <path d="M280 0 C 400 85, 416 330, 366 459" fill="none" stroke="var(--white)" stroke-width="6"/>
  </svg>

  <div class="brand">
    <span class="brand__name">KORIDAN</span>
    <span class="brand__sub">REAL ESTATE</span>
  </div>

  <p class="headline">Curios to know what your<br>home is worth?</p>
  <p class="teaser">START OF NEW YEAR WITH <strong>JASVEER SANDHU</strong> AND FIND OUT!</p>

  <div class="cta">
    <span>CALL ME NOW!</span>
    <svg viewBox="0 0 24 24" aria-hidden="true">
      <circle cx="12" cy="12" r="10.5" fill="none" stroke="var(--maroon)" stroke-width="2"/>
      <path d="M8.5 7 l2 2 -1.2 1.5 c.8 1.6 2 2.8 3.6 3.6 l1.5-1.2 2 2 -1.3 1.6 c-4 -.5 -7.4-3.9-7.9-7.9 Z" fill="var(--maroon)"/>
    </svg>
    <span>03 9142 7305</span>
  </div>
  <p class="cta__note">For Free property Appraisal</p>
</section>

<section class="flyer flyer--back back">
  <div class="brand">
    <span class="brand__name">KORIDAN</span>
    <span class="brand__sub">REAL ESTATE</span>
  </div>

  <ul class="contact-list">
    <li>
      <svg viewBox="0 0 24 24" aria-hidden="true"><circle cx="12" cy="12" r="10.5" fill="none" stroke="var(--white)" stroke-width="2"/><path d="M8.5 7 l2 2 -1.2 1.5 c.8 1.6 2 2.8 3.6 3.6 l1.5-1.2 2 2 -1.3 1.6 c-4 -.5 -7.4-3.9-7.9-7.9 Z" fill="var(--white)"/></svg>
      03 9142 7305
    </li>
    <li>
      <svg viewBox="0 0 24 24" aria-hidden="true"><circle cx="12" cy="12" r="11" fill="var(--white)"/><rect x="6.5" y="8" width="11" height="8" fill="none" stroke="var(--navy)" stroke-width="1.5"/><path d="M6.5 8 L12 12.5 17.5 8" fill="none" stroke="var(--navy)" stroke-width="1.5"/></svg>
      info@koridanrealestate.example.au
    </li>
    <li>
      <svg viewBox="0 0 24 24" aria-hidden="true"><circle cx="12" cy="12" r="11" fill="var(--white)"/><circle cx="12" cy="12" r="6.5" fill="none" stroke="var(--navy)" stroke-width="1.3"/><ellipse cx="12" cy="12" rx="2.8" ry="6.5" fill="none" stroke="var(--navy)" stroke-width="1.3"/><path d="M5.5 12 H18.5" stroke="var(--navy)" stroke-width="1.3"/></svg>
      www.koridanrealestate.example.au
    </li>
  </ul>

  <div class="agent-photo" role="img" aria-label="Portrait photo of the agent in a blue suit and striped tie"></div>

  <div class="footer-band">
    <span class="footer-band__address">9 / 386 Barwin Rd Truganina, Victoria, Australia 3029</span>
    <span class="footer-band__agent">Jasveer Sandhu, Realtor</span>
  </div>
</section>

</body>
</html>
```